**Launching Worlds Greatest Eco Friendly Doggy Poop Bags!**

We are an eco-friendly company located in San Francisco, California. We are launching a new line of amazing new eco-friendly doggy poop bags. They are biodegradable and super easy to open. Additionally they are strong, durable and light weight. We would like to see some designs for a box and logo under the label "Bright Meadow". We'd like to see the colors green and blue used to promote earth friendly product.

Target Market(s)

Dog owners

Industry/Entity Type

It Company

Colors
00a990
0592cd
9bcb3c

Requirements
Must have
• Would like to see a happy looking dog and portray earth friendly images. Cartoon type images. Would like fun, happy, cartoon like dog and Bright Meadow Logo to go in front of the box.
Nice to have
• Images of dog prints or happy dog(s) that we can put in different areas of the box. (examples of competitors boxes included)
Should not have
• Not fancy or formal.

```html
<!DOCTYPE html>
<html lang="en">
<head>
<meta charset="utf-8">
<title>Bright Meadow – Poop Bag Box Panels</title>
<link href="https://fonts.googleapis.com/css2?family=Oswald:wght@400;500;600&display=swap" rel="stylesheet">
<style>
  :root{
    --teal:#2bb59c;
    --teal-deep:#00a990;
    --leaf:#7cb342;
    --leaf-bright:#9bcb3c;
    --sky:#0592cd;
    --navy:#1d4f95;
    --paper:#f3f3f1;
    --side:#e6e6e6;
    --band:#444444;
    --page:#d9d9d9;
    --white:#ffffff;
  }
  *{box-sizing:border-box;margin:0;padding:0}
  html,body{width:1190px;height:1200px;overflow:hidden}
  body{background:var(--page);font-family:"Oswald",sans-serif;position:relative}

  .panel{position:absolute;top:50px;height:1100px;overflow:hidden}
  .front{left:90px;width:720px;background:var(--paper)}
  .side{left:820px;width:250px;background:var(--side)}

  .front__band{position:absolute;left:0;top:0;width:720px;height:420px}
  .brand-name{position:absolute;left:0;top:130px;width:720px;text-align:center;
    color:var(--white);font-weight:500;font-size:92px;line-height:1;letter-spacing:1px;white-space:nowrap}
  .count-badge{position:absolute;left:210px;top:262px;width:300px;height:120px}
  .count-badge__number{position:absolute;left:0;top:16px;width:300px;text-align:center;
    color:var(--white);font-size:40px;font-weight:500;line-height:1}
  .count-badge__label{position:absolute;left:0;top:66px;width:300px;text-align:center;
    color:var(--white);font-size:17px;font-weight:500;letter-spacing:.5px;white-space:nowrap}

  .product-window{position:absolute;left:90px;top:370px;width:540px;height:540px;border-radius:50%;
    border:5px solid var(--leaf);
    background:radial-gradient(circle at 50% 45%,#9ccc4a 0%,#6fa832 60%,#4f8a24 100%)}
  .globe{position:absolute;left:-120px;top:830px;width:960px;height:520px;border-radius:50%;
    background:linear-gradient(180deg,#7ec03a 0%,#5aa52c 45%,#3f9ad6 100%)}
  .mascot{position:absolute;left:200px;top:560px;width:310px;height:370px;border-radius:40px;
    background:linear-gradient(180deg,#c98a4e 0%,#a8683a 100%);border:6px solid var(--white)}

  .front__footer{position:absolute;left:0;bottom:0;width:720px;height:70px;background:var(--band);
    color:var(--white);font-size:22px;font-weight:400;display:flex;align-items:center;justify-content:center;letter-spacing:.3px;white-space:nowrap}

  .spec-label{position:absolute;left:44px;top:70px;width:78px;height:360px;background:var(--navy);
    display:flex;flex-direction:column;align-items:center;justify-content:center;gap:8px;
    writing-mode:vertical-rl;transform:rotate(180deg);white-space:nowrap}
  .spec-label__title{color:var(--white);font-size:21px;font-weight:600;line-height:1}
  .spec-label__line{line-height:1}
  .spec-label__size{color:var(--white);font-size:17px;font-weight:500}
  .spec-label__note{color:var(--leaf-bright);font-size:13px;font-weight:500;margin-top:8px}
  .side__tagline{position:absolute;left:140px;top:70px;height:360px;writing-mode:vertical-rl;transform:rotate(180deg);
    text-align:center;color:var(--leaf);font-size:16px;letter-spacing:5px;font-weight:400;white-space:nowrap}
  .side__brand{position:absolute;left:80px;top:450px;height:400px;writing-mode:vertical-rl;transform:rotate(180deg);
    text-align:center;color:var(--leaf);font-size:58px;font-weight:500;line-height:1;white-space:nowrap}
  .side__mascot{position:absolute;left:20px;top:870px;width:210px;height:230px;border-radius:30px 30px 0 0;
    background:linear-gradient(180deg,#c98a4e 0%,#a8683a 100%)}
</style>
</head>
<body>
  <section class="panel front">
    <svg class="front__band" viewBox="0 0 720 420" aria-hidden="true">
      <path d="M0 0H720V340Q360 250 0 340Z" fill="var(--teal)"/>
      <path d="M215 300Q360 265 505 300Q500 385 360 390Q220 385 215 300Z" fill="var(--leaf)"/>
    </svg>
    <h1 class="brand-name">Bright Meadow</h1>
    <div class="count-badge">
      <div class="count-badge__number">250</div>
      <div class="count-badge__label">ECO-FRIENDLY DOGGY POOP BAGS</div>
    </div>
    <div class="product-window" role="img" aria-label="Window view of green biodegradable bag rolls with recycle paw print"></div>
    <div class="globe" role="img" aria-label="Cartoon green and blue earth"></div>
    <div class="mascot" role="img" aria-label="Happy cartoon dog mascot with green collar and bell"></div>
    <p class="front__footer">LOREM IPSUM DOLOR SIT AMET CONSECTETUR ADIPISCING ELIT</p>
  </section>

  <section class="panel side">
    <div class="spec-label">
      <span class="spec-label__title">LOREM IPSUM DOLOR SIT AMET</span>
      <span class="spec-label__line"><span class="spec-label__size">(32" X 32")</span><span class="spec-label__note">CONSECTETUR ADIPISCING</span></span>
    </div>
    <p class="side__tagline">QUAMVIS ENIM DEPRA</p>
    <p class="side__brand">Bright Meadow</p>
    <div class="side__mascot" role="img" aria-label="Cartoon dog mascot peeking in from the bottom"></div>
  </section>
</body>
</html>
```